Bramford Holloway Inc. needs an innovative idea for letterhead and visiting cards.

Bramford Holloway Inc. is a Canadian brand since 2007. It is a renown dealer of kids and office furniture locally. Moreover, exporting electric fixtures e.g. switches, LED's, down-lights etc. to Middle East and Africa. We have initiated a number of steps including re-branding, to boost our export in 2020. We have successfully designed our new logo a few months ago through 'Mockplanet' and now we are looking for an innovative idea for a letterhead.
Some key points:
• Red, black and white are the three colors used in all our packaging and furniture. (grey is optional)
• Shouldn’t be too wide.
• Use of watermark is preferable.
• You can visit our North American site at www.bramfordhollowayinc.com. Export website of the company will be launched soon. www.bramfordhollowayinc.ca
• Same letterhead will be used locally and internationally.
• Our new logo and sample packaging is attached.

```html
<!DOCTYPE html>
<html lang="en">
<head>
<meta charset="utf-8">
<title>Bramford Holloway Inc. Letterhead</title>
<link rel="stylesheet" href="https://fonts.googleapis.com/css2?family=Arimo:wght@400;700&display=swap">
<style>
  :root {
    --stage: #dcdedf;
    --paper: #ffffff;
    --red: #d7261e;
    --red-deep: #9c1a16;
    --ink: #3a3a3a;
    --body: #6d6d6d;
    --grey: #9a9a9a;
    --light-grey: #c7c7c7;
    --black: #1b1b1b;
    --watermark: rgba(215, 38, 30, 0.06);
  }
  * { box-sizing: border-box; margin: 0; padding: 0; }
  html, body { width: 1200px; height: 784px; overflow: hidden; }
  body {
    background: var(--stage);
    font-family: "Arimo", Arial, sans-serif;
    display: flex; align-items: center; justify-content: center;
  }
  .letterhead {
    position: relative;
    width: 523px; height: 740px;
    background: var(--paper);
    box-shadow: 0 6px 18px rgba(0,0,0,0.18);
    overflow: hidden;
  }
  .corner { position: absolute; display: block; }
  .corner--top { top: 0; right: 0; }
  .corner--bottom { bottom: 0; left: 0; }
  .brand {
    position: absolute; top: 40px; left: 44px;
    display: flex; align-items: center; gap: 10px;
  }
  .brand__mark { width: 30px; height: 30px; background: var(--red); border-radius: 4px; }
  .brand__name {
    font-size: 17px; line-height: 1.1; font-weight: 400; color: var(--ink);
    letter-spacing: 1px; text-transform: uppercase;
  }
  .watermark {
    position: absolute; left: 150px; top: 300px;
    width: 230px; height: 230px;
    background: var(--watermark); border-radius: 18px;
  }
  .letter-body {
    position: absolute; top: 104px; left: 44px; width: 432px;
    font-size: 9.6px; line-height: 1.55; color: var(--body);
  }
  .letter-body p + p { margin-top: 12px; }
  .signature {
    position: absolute; left: 150px; top: 520px;
    width: 160px; height: 44px;
    background: linear-gradient(90deg, rgba(120,120,120,0.14), rgba(120,120,120,0.03));
    border-radius: 4px;
  }
  .footer {
    position: absolute; left: 0; right: 0; bottom: 80px;
    display: flex; flex-direction: column; align-items: center; gap: 6px;
  }
  .footer__icons { display: flex; align-items: center; gap: 12px; }
  .footer__rule { width: 70px; height: 1px; background: var(--grey); }
  .footer__icon { width: 14px; height: 14px; display: block; }
  .footer__address { font-size: 9.5px; font-weight: 700; color: var(--red); }
  .footer__contact { font-size: 8.6px; color: var(--ink); }
</style>
</head>
<body>
  <main class="letterhead">
    <svg class="corner corner--top" width="250" height="80" viewBox="0 0 250 80" aria-hidden="true">
      <defs>
        <linearGradient id="redTop" x1="0" y1="0" x2="1" y2="1">
          <stop offset="0" stop-color="#d7261e"/>
          <stop offset="1" stop-color="#9c1a16"/>
        </linearGradient>
      </defs>
      <polygon points="0,0 250,0 250,38 200,46" fill="url(#redTop)"/>
      <polyline points="0,0 200,50 250,42" fill="none" stroke="#1b1b1b" stroke-width="3"/>
      <polyline points="0,0 200,56 250,48" fill="none" stroke="#9a9a9a" stroke-width="3"/>
      <polyline points="0,0 200,62 250,54" fill="none" stroke="#c7c7c7" stroke-width="2"/>
    </svg>

    <div class="brand">
      <span class="brand__mark"></span>
      <span class="brand__name">Bramford<br>Holloway Inc.</span>
    </div>

    <div class="watermark" aria-hidden="true"></div>

    <section class="letter-body">
      <p>Lorem Ipsum is simply dummy text of the printing and typesetting industry. Lorem Ipsum has been the industry's standard dummy text ever since the 1500s, when an unknown printer took a galley of type and scrambled it to make a type specimen book. It has survived not only five centuries, but also the leap into electronic typesetting, remaining essentially unchanged. It was popularised in the 1960s with the release of Lettrane sheets containing Lorem Ipsum passages, and more recently with desktop publishing software like Pagewright Studio including versions of Lorem Ipsum.</p>
      <p>It is a long established fact that a reader will be distracted by the readable content of a page when looking at its layout. The point of using Lorem Ipsum is that it has a more-or-less normal distribution of letters, as opposed to using 'Content here, content here', making it look like readable English. Many desktop publishing packages and web page editors now use Lorem Ipsum as their default model text, and a search for 'lorem ipsum' will uncover many web sites still in their infancy. Various versions have evolved over the years, sometimes by accident, sometimes on purpose (injected humour and the like).</p>
      <p>Contrary to popular belief, Lorem Ipsum is not simply random text. It has roots in a piece of classical Latin literature from 45 BC, making it over 2000 years old. Martin Elsworth, a Latin professor at Kestrel Hill College in Ontario, looked up one of the more obscure Latin words, consectetur, from a Lorem Ipsum passage, and going through the cites of the word in classical literature, discovered the undoubtable source. Lorem Ipsum comes from sections 1.10.32 and 1.10.33 of "de Finibus Bonorum et Malorum" structures, to generate Lorem Ipsum which looks reasonable. The generated Lorem Ipsum is therefore always free from repetition, injected humour, or non-characteristic words etc.</p>
    </section>

    <div class="signature" role="img" aria-label="Handwritten signature of the sender"></div>

    <footer class="footer">
      <div class="footer__icons">
        <span class="footer__rule"></span>
        <svg class="footer__icon" viewBox="0 0 14 14" aria-label="Address">
          <circle cx="7" cy="7" r="7" fill="#d7261e"/>
          <path d="M7 3.2a2.4 2.4 0 0 0-2.4 2.4C4.6 7.4 7 10.6 7 10.6s2.4-3.2 2.4-5A2.4 2.4 0 0 0 7 3.2z" fill="#fff"/>
          <circle cx="7" cy="5.6" r="0.9" fill="#d7261e"/>
        </svg>
        <svg class="footer__icon" viewBox="0 0 14 14" aria-label="Phone">
          <circle cx="7" cy="7" r="7" fill="#d7261e"/>
          <path d="M4.6 3.6l1.4 1.6-.7 1a5 5 0 0 0 2.5 2.5l1-.7 1.6 1.4-.8 1.2C6.6 10.4 3.6 7.4 3.4 4.4z" fill="#fff"/>
        </svg>
        <svg class="footer__icon" viewBox="0 0 14 14" aria-label="Email">
          <circle cx="7" cy="7" r="7" fill="#d7261e"/>
          <rect x="3.6" y="4.6" width="6.8" height="4.8" fill="#fff"/>
          <polyline points="3.6,4.6 7,7.4 10.4,4.6" fill="none" stroke="#d7261e" stroke-width="0.8"/>
        </svg>
        <svg class="footer__icon" viewBox="0 0 14 14" aria-label="Website">
          <circle cx="7" cy="7" r="7" fill="#d7261e"/>
          <circle cx="7" cy="7" r="3.6" fill="none" stroke="#fff" stroke-width="0.9"/>
          <ellipse cx="7" cy="7" rx="1.5" ry="3.6" fill="none" stroke="#fff" stroke-width="0.8"/>
          <line x1="3.4" y1="7" x2="10.6" y2="7" stroke="#fff" stroke-width="0.8"/>
        </svg>
        <span class="footer__rule"></span>
      </div>
      <p class="footer__address">48 Larkspur Way, Unit 206, Fernhill, ON K2P 4R8</p>
      <p class="footer__contact">+1 (888) 240-3176 | info@bramfordhollowayinc.com</p>
      <p class="footer__contact">www.bramfordhollowayinc.com</p>
    </footer>

    <svg class="corner corner--bottom" width="250" height="80" viewBox="0 0 250 80" aria-hidden="true">
      <defs>
        <linearGradient id="redBottom" x1="1" y1="1" x2="0" y2="0">
          <stop offset="0" stop-color="#d7261e"/>
          <stop offset="1" stop-color="#9c1a16"/>
        </linearGradient>
      </defs>
      <polygon points="250,80 0,80 0,42 50,34" fill="url(#redBottom)"/>
      <polyline points="250,80 50,30 0,38" fill="none" stroke="#1b1b1b" stroke-width="3"/>
      <polyline points="250,80 50,24 0,32" fill="none" stroke="#9a9a9a" stroke-width="3"/>
      <polyline points="250,80 50,18 0,26" fill="none" stroke="#c7c7c7" stroke-width="2"/>
    </svg>
  </main>
</body>
</html>
```